Design a 4-page brochure for Juniper Ridge Fund

Please use the content from the Updated Brochure attachment to design a 4-page 4-color glossy letter sized brochure for Juniper Ridge Fund. The content and concept of the brochure are in the attached word document. Additional photos are attached, and a logo for the fund will be forthcoming (the logo is currently a contest on ArtHive)
We own the attached photos that can be used in brochure.

Target Market(s)

Investors

Industry/Entity Type

Investment

```html
<!DOCTYPE html>
<html lang="en">
<head>
<meta charset="utf-8">
<title>Juniper Ridge Fund – Brochure</title>
<link href="https://fonts.googleapis.com/css2?family=Lato:wght@400;700&family=Oswald:wght@200;300&display=swap" rel="stylesheet">
<style>
:root{
  --stage:#5d5d5d;
  --teal:#4d8781;
  --teal-light:#b2d9d6;
  --teal-link:#4ba6a1;
  --paper:#ffffff;
  --paper-soft:#f3f3f3;
  --ink:#222;
  --table-head:#5dbdb6;
  --photo-people:linear-gradient(90deg,#9b3a2a 0%,#6f6a55 25%,#8fae3a 45%,#3d6e6c 70%,#2f5b5e 100%);
  --photo-city:linear-gradient(180deg,#5860b8 0%,#6b63c4 35%,#c89a5a 62%,#3b3570 80%,#27304a 100%);
  --photo-chart:linear-gradient(135deg,#7b838c 0%,#2c2f35 45%,#aab1b8 100%);
  --photo-portrait:linear-gradient(160deg,#4c6a8c 0%,#c9a98a 50%,#2d3a55 100%);
  --photo-portrait-b:linear-gradient(160deg,#c3ccb5 0%,#d3b79b 50%,#1f2f4a 100%);
  --photo-portrait-c:linear-gradient(160deg,#6a7a4a 0%,#d39a7a 50%,#7c2a22 100%);
}
*{box-sizing:border-box;margin:0;padding:0}
html,body{width:1052px;height:1200px;overflow:hidden}
body{background:var(--stage);font-family:"Lato",sans-serif;color:var(--ink);position:relative}
.spread{position:absolute;width:770px;height:504px;background:var(--paper);overflow:hidden}
.spread--cover{left:108px;top:60px}
.spread--inside{left:192px;top:612px}
.abs{position:absolute}
.photo{position:absolute}

/* cover */
.cover-block{left:0;top:0;width:385px;height:140px;background:var(--teal-light)}
.brand{left:414px;top:98px;display:flex;align-items:center;gap:8px}
.brand__square{width:30px;height:30px;border:2px solid var(--teal)}
.brand__name{font-family:"Lato",sans-serif;font-weight:700;font-size:27px;letter-spacing:1px;color:var(--teal)}
.cover-url{left:32px;top:149px;font-size:13.5px;color:var(--teal-link)}
.cover-band{left:0;top:175px;width:770px;height:25px;background:var(--teal)}
.photo--people{left:0;top:200px;width:385px;height:141px;background:var(--photo-people)}
.photo--city{left:385px;top:200px;width:385px;height:141px;background:var(--photo-city)}
.cover-panel{left:0;top:341px;width:770px;height:98px;background:var(--teal);color:#fff}
.founders{left:32px;top:15px;width:315px}
.founders h2{font-size:12px;font-weight:700;margin-bottom:8px}
.founders p{font-size:7.3px;line-height:1.5}
.tagline{left:406px;top:12px;font-family:"Oswald",sans-serif;font-weight:200;font-size:21px;line-height:1.24;text-transform:uppercase}
.copyright{left:32px;top:482px;font-size:7px;color:var(--teal-link)}

/* inside */
.photo--growth{left:0;top:0;width:385px;height:168px;background:var(--photo-chart)}
.fund-panel{left:0;top:168px;width:385px;height:164px;background:var(--teal);color:#fff}
.fund-panel h2{position:absolute;left:20px;top:16px;font-size:10.5px;font-weight:400}
.fund-col{position:absolute;top:36px;width:152px;font-size:5.2px;line-height:1.6;text-align:justify}
.fund-col p+p{margin-top:6px}
.fund-col--a{left:20px}
.fund-col--b{left:200px}
.returns{position:absolute;border-collapse:collapse;font-size:4.6px}
.returns caption{caption-side:top;text-align:left}
.returns caption span{border:0.6px solid #333;padding:0 2px;display:inline-block}
.returns th{background:var(--table-head);color:#fff;font-weight:400;text-align:left;padding:1px 3px;line-height:1.05}
.returns td{padding:1.5px 3px;border-bottom:0.8px solid #333;white-space:nowrap}
.returns tr.total td{border-bottom:none}
.returns--two{left:24px;top:348px;width:288px}
.returns--four{left:76px;top:412px;width:288px}
.disclaimer{left:20px;top:492px;width:350px;font-size:3.6px;line-height:1.3}
.cell{position:absolute;width:193px;height:168px}
.cell--teal{background:var(--teal);color:#fff}
.cell--white{background:var(--paper)}
.cell--soft{background:var(--paper-soft)}
.bio{padding:14px 10px 0 10px;font-size:4.9px;line-height:1.6;text-align:justify}
.bio p+p{margin-top:6px}
.bio b{font-weight:700}
.portrait-frame{position:absolute;left:22px;top:14px;width:148px;height:142px;border-top:1px solid #111;border-bottom:1px solid #111;padding:4px 7px}
.portrait{width:100%;height:100%}
</style>
</head>
<body>

<section class="spread spread--cover">
  <div class="abs cover-block"></div>
  <div class="abs brand"><span class="brand__square"></span><span class="brand__name">JUNIPER RIDGE</span></div>
  <div class="abs cover-url">www.juniperridgefund.com</div>
  <div class="abs cover-band"></div>
  <div class="photo photo--people" role="img" aria-label="Three founding partners in suits talking in a colourful office"></div>
  <div class="photo photo--city" role="img" aria-label="City skyline lit at dusk across the water"></div>
  <div class="abs cover-panel">
    <div class="abs founders">
      <h2>FOUNDING MEMBERS OF JUNIPER RIDGE</h2>
      <p>Messrs. Marsh, Halloran and Dekker founded Juniper Ridge in 2010. Their debut fund was a boutique venture capital fund. Juniper Ridge is building upon the success of its first fund with the launch of Fund II, a venture debt fund that invests in early to mid-stage companies and securities with preferred returns.</p>
    </div>
    <div class="abs tagline">Now you can finally earn substantial<br>monthly returns while realizing solid<br>capital growth</div>
  </div>
  <div class="abs copyright">© 2016 Juniper Ridge Funds</div>
</section>

<section class="spread spread--inside">
  <div class="photo photo--growth" role="img" aria-label="Businessman beside a rising arrow over small building icons and a city view"></div>
  <div class="abs fund-panel">
    <h2>JUNIPER RIDGE FUND II</h2>
    <div class="fund-col fund-col--a">
      <p>Messrs. Marsh, Halloran and Dekker founded Juniper Ridge in 2010. Their debut fund was a boutique venture capital fund. Juniper Ridge is building upon the success of its first fund with the launch of Fund II, a venture debt fund that invests in early to mid-stage companies and securities with preferred returns.</p>
      <p>Fund II pays its investors a 9% annual return on a monthly basis, and a preference of 1.25x on repayments made in 3 years or less. If the repayment is extended beyond 3 years, the investors will be paid a 12% annual return on a monthly basis, with a preference of 1.5x on repayment.</p>
    </div>
    <div class="fund-col fund-col--b">
      <p>The fund is obligated to liquidate its portfolio to repay investors within five years of the date of their investment.</p>
      <p>The minimum investment in Fund II is fifty thousand dollars ($50,000). The first three years of interest is paid from a reserve and liquidations within the fund's portfolio will be used to pay the preferential returns and remaining interest payments. Investors should note that a sale of any of the Fund's assets could pay the preferential returns before the 3-year maturity date, and such early repayment would terminate the Fund's obligation to make further interest payments.</p>
    </div>
  </div>

  <table class="returns returns--two">
    <caption><span>Exit in 2 Years</span></caption>
    <tr><th></th><th>Investment<br>Amount</th><th>Interest<br>Rate</th><th>Interest<br>Received</th><th>Preference<br>Rate</th><th>Preference<br>Amount</th><th>Total<br>Return</th><th>Return on<br>Investment</th></tr>
    <tr><td>Year 1</td><td>$100,000</td><td>9%</td><td>$9,000</td><td></td><td></td><td></td><td></td></tr>
    <tr><td>Year 2</td><td></td><td>9%</td><td>$9,000</td><td>1.25</td><td>$125,000</td><td></td><td></td></tr>
    <tr class="total"><td>Total:</td><td></td><td></td><td>$18,000</td><td></td><td>$125,000</td><td>$143,000</td><td>43%</td></tr>
  </table>

  <table class="returns returns--four">
    <caption><span>Exit in 4 Years</span></caption>
    <tr><th></th><th>Investment<br>Amount</th><th>Interest<br>Rate</th><th>Interest<br>Received</th><th>Preference<br>Rate</th><th>Preference<br>Amount</th><th>Total<br>Return</th><th>Return on<br>Investment</th></tr>
    <tr><td>Year 1</td><td>$100,000</td><td>9%</td><td>$9,000</td><td></td><td></td><td></td><td></td></tr>
    <tr><td>Year 2</td><td></td><td>9%</td><td>$9,000</td><td></td><td></td><td></td><td></td></tr>
    <tr><td>Year 3</td><td></td><td>9%</td><td>$9,000</td><td></td><td></td><td></td><td></td></tr>
    <tr><td>Year 4</td><td></td><td>12%</td><td>$12,000</td><td>1.5</td><td>$150,000</td><td></td><td></td></tr>
    <tr class="total"><td>Total:</td><td></td><td></td><td>$39,000</td><td></td><td>$150,000</td><td>$189,000</td><td>89%</td></tr>
  </table>

  <p class="abs disclaimer">The statements in this brochure are forward-looking statements by the Fund's management, which cannot be relied upon to accurately project actual future returns on an investment in the Fund (see Risk Factors in the Fund's PPM).</p>

  <div class="cell cell--teal" style="left:385px;top:0">
    <div class="bio">
      <p><b>Mr. Dekker</b> is a seasoned CFO and veteran of the financial community with more than thirty years of experience in pioneering new financial vehicles and structures. Early in his career he helped pioneer pass-through and electronic delivery systems for national mortgage agencies. He subsequently turned to securitizing mortgages, where he successfully structured four REMIC security offerings as the CFO of a life insurance company, and was among the first in the nation to use the newly legislated REMIC pass-through structure.</p>
      <p>Later, Mr. Dekker assisted Mr. Marsh's firm in structuring the nation's first mixed mortgage pool, overseeing both loan origination and underwriting, and well as providing the modeling necessary to verify the viability of the pool's cash flows to achieve investment grade ratings. Mr. Dekker managed the team that structured the financing for a national redevelopment program.</p>
    </div>
  </div>
  <div class="cell cell--soft" style="left:577px;top:0">
    <div class="portrait-frame"><div class="portrait" style="background:var(--photo-portrait)" role="img" aria-label="Portrait of Mr. Dekker in a suit"></div></div>
  </div>

  <div class="cell cell--white" style="left:385px;top:168px">
    <div class="portrait-frame"><div class="portrait" style="background:var(--photo-portrait-b)" role="img" aria-label="Portrait of Mr. Halloran outdoors in a suit"></div></div>
  </div>
  <div class="cell cell--teal" style="left:577px;top:168px">
    <div class="bio">
      <p><b>Mr. Halloran</b> brings over twenty years of entrepreneurial experience to the Fund. He has a background in implementing strategic plans to drive enterprise value, with an emphasis on sales management and business development. Mr. Halloran has been a co-founder in a number of early stage companies, raising over thirty million dollars in angel financing.</p>
      <p>At Corvane Mr. Halloran chaired the Sales Advisory Council and helped a regional health plan write a new procedure into policy. He was a senior sales representative and winner of his company's top sales award. Mr. Halloran was responsible for sales at Halvern Medical and for client support and financial research at a regional bank. He started his career as a pricing analyst and won a national championship in rowing at university.</p>
    </div>
  </div>

  <div class="cell cell--soft" style="left:385px;top:336px">
    <div class="bio">
      <p><b>Mr. Marsh</b> is a founder of companies in numerous markets, including citrus, finance, education, publishing, and technology. He is a pioneer in structured finance, originating the first commercial mortgage conduit pool in the nation and securing a one billion dollar line of credit from a major investment bank. He founded a firm that helped structure the financing for a national redevelopment program, which provided housing for thousands of families.</p>
      <p>Mr. Marsh founded Brightkids Magazine, leading its expansion in the US and abroad. The publication was circulated in more than thirty countries, with a readership in the millions. Mr. Marsh is a co-founder of three technology companies and two charter schools, the later of which is consistently ranked in the top fifty schools in the nation by leading national publications.</p>
    </div>
  </div>
  <div class="cell cell--white" style="left:577px;top:336px">
    <div class="portrait-frame"><div class="portrait" style="background:var(--photo-portrait-c)" role="img" aria-label="Portrait of Mr. Marsh smiling outdoors"></div></div>
  </div>
</section>

</body>
</html>
```